Brightmere Pictures Business Card

Hello,

i would like to have a dynamic, creative but tasteful card, colour used, front and back. I have attached a sample card that I liked very much from another individual to give you an idea of the theme/approach, but not colour. Ideally the graphic elements of the Brightmere Logo are brought into the design.

Target Market(s)

North America

Industry/Entity Type

Film Production

Contact Information for Business Card

Nadia Pellwick
President/Founder
Brightmere Pictures Inc.
403 555 2917
nadia@brightmerepictures.tv

Font styles to use
Sans Serif

Colors
6b449b
5c5c5c
fdfdfd
000000

Requirements
Must have
• Logo, name, Company name, email and cell number. no Address line to be included.
Should not have
• any unrelated GFX elements, serif fonts

```html
<!DOCTYPE html>
<html lang="en">
<head>
<meta charset="utf-8">
<title>Brightmere Pictures Business Card</title>
<link href="https://fonts.googleapis.com/css2?family=Lato:wght@400;700;900&display=swap" rel="stylesheet">
<style>
  :root {
    --brand-purple: #56248b;
    --ink-grey: #5c5c5c;
    --paper: #fdfdfd;
    --backdrop: #e9e6e1;
    --shadow: rgba(0, 0, 0, 0.18);
  }
  * { box-sizing: border-box; margin: 0; padding: 0; }
  html, body {
    width: 1200px;
    height: 911px;
    overflow: hidden;
    background: var(--backdrop);
    font-family: "Lato", sans-serif;
  }
  .canvas {
    position: relative;
    width: 1200px;
    height: 911px;
    display: flex;
    align-items: center;
    justify-content: center;
    gap: 80px;
  }
  .card {
    position: relative;
    overflow: hidden;
    box-shadow: 0 10px 28px var(--shadow);
  }
  .card-front {
    width: 340px;
    height: 560px;
    background: var(--brand-purple);
    color: var(--paper);
    text-align: center;
  }
  .contact-block {
    position: absolute;
    top: 62px;
    left: 0;
    right: 0;
    display: flex;
    flex-direction: column;
    align-items: center;
  }
  .icon {
    width: 14px;
    height: 14px;
    fill: var(--paper);
    margin-bottom: 6px;
  }
  .person-name {
    font-weight: 700;
    font-size: 25px;
    letter-spacing: 0.3px;
  }
  .person-title {
    font-weight: 400;
    font-size: 15px;
    margin-top: 2px;
    margin-bottom: 52px;
  }
  .contact-line {
    font-size: 14px;
    margin-bottom: 16px;
  }
  .front-disc {
    position: absolute;
    left: 50%;
    bottom: -170px;
    width: 340px;
    height: 340px;
    transform: translateX(-50%);
    border-radius: 50%;
    background: var(--paper);
  }
  .card-back {
    width: 560px;
    height: 340px;
    background: var(--paper);
    display: flex;
    align-items: center;
    justify-content: center;
    gap: 16px;
  }
  .brand-mark {
    width: 30px;
    height: 30px;
    border-radius: 50%;
    background: var(--brand-purple);
  }
  .brand-name {
    font-weight: 900;
    font-size: 46px;
    color: var(--ink-grey);
    letter-spacing: -0.5px;
  }
</style>
</head>
<body>
<main class="canvas">
  <section class="card card-front" aria-label="Card front">
    <div class="contact-block">
      <svg class="icon" viewBox="0 0 16 16" aria-hidden="true"><circle cx="8" cy="5" r="3.5"/><path d="M1 16c0-4 3-6.5 7-6.5s7 2.5 7 6.5z"/></svg>
      <p class="person-name">Nadia Pellwick</p>
      <p class="person-title">President/Founder</p>

      <svg class="icon" viewBox="0 0 16 16" aria-hidden="true"><path d="M3.5 1l3 3-1.8 2a9 9 0 0 0 5.3 5.3l2-1.8 3 3-2 2C6 14.5 1.5 10 1.5 3z"/></svg>
      <p class="contact-line">403 555 2917</p>

      <svg class="icon" viewBox="0 0 16 16" aria-hidden="true"><rect x="1" y="3" width="14" height="10"/><path d="M1 3l7 6 7-6" fill="none" stroke="#56248b" stroke-width="1.4"/></svg>
      <p class="contact-line">nadia@brightmerepictures.tv</p>

      <svg class="icon" viewBox="0 0 16 16" aria-hidden="true"><circle cx="8" cy="8" r="7"/><path d="M1 8h14M8 1c-3 4-3 10 0 14M8 1c3 4 3 10 0 14" fill="none" stroke="#56248b" stroke-width="1"/></svg>
      <p class="contact-line">brightmerepictures.tv</p>
    </div>
    <div class="front-disc" aria-hidden="true"></div>
  </section>

  <section class="card card-back" aria-label="Card back">
    <span class="brand-mark" aria-hidden="true"></span>
    <p class="brand-name">Brightmere Pictures</p>
  </section>
</main>
</body>
</html>
```